CBD wholesaling/distribution website

I need a clean , professional looking website that is modern / but not cannabis themed. we are steering clear of anything green.

Coding

Coded - Design and coding required

Number of Pages Required

1 page

```html
<!DOCTYPE html>
<html lang="en">
<head>
<meta charset="utf-8">
<title>Nordline – Your Trusted CBD Source</title>
<link href="https://fonts.googleapis.com/css2?family=Open+Sans:wght@400;600;700&display=swap" rel="stylesheet">
<style>
:root{
  --blue:#1186ef;
  --blue-title:#1a88e6;
  --navy:#0c3c78;
  --ink:#1c1c1c;
  --text:#333;
  --muted:#f2f2f2;
  --line:#bdbdbd;
  --white:#fff;
}
*{box-sizing:border-box;margin:0;padding:0}
html,body{width:1200px;height:2816px;overflow:hidden}
body{font-family:"Open Sans",Arial,sans-serif;color:var(--text);background:var(--white);position:relative}
.section{position:absolute;left:0;width:1200px}
.abs{position:absolute}
.center{left:0;width:1200px;text-align:center}
.fill{position:absolute;inset:0}

.topbar{top:0;height:43px;background:var(--blue);color:var(--white);font-size:12.5px}
.topbar .contact-item{top:12px;display:flex;align-items:center;gap:7px}
.topbar .divider{left:203px;top:12px;width:1px;height:17px;background:rgba(255,255,255,.7)}
.social{top:9px;right:99px;display:flex;gap:8px}
.social span{width:25px;height:25px;border:1.6px solid var(--white);border-radius:50%;display:block}

.header{top:43px;height:109px;background:var(--white)}
.brand{left:98px;top:18px;display:flex;align-items:center;gap:14px}
.brand-mark{width:62px;height:62px;background:var(--blue)}
.brand-name{font-size:22px;font-weight:600;color:var(--blue);line-height:1.1}
.brand-tag{font-size:15.5px;font-weight:600;color:var(--blue);margin-top:2px}
.nav{right:99px;top:48px;display:flex;font-size:12px;color:var(--ink)}
.nav a{color:var(--ink);text-decoration:none}
.nav .sep{margin:0 24px;color:var(--ink)}

.hero{top:152px;height:492px;overflow:hidden}
.hero-bg{background:linear-gradient(180deg,#9a9a96 0%,#7d7a70 22%,#66615a 45%,#4a4640 75%,#36332f 100%)}
.hero-shade{background:linear-gradient(90deg,rgba(0,0,0,.4) 0%,rgba(0,0,0,0) 55%)}
.hero h1{left:98px;top:146px;font-size:31px;font-weight:700;color:var(--white);letter-spacing:.3px}
.hero p{left:98px;top:192px;width:440px;font-size:12.5px;line-height:22.4px;color:var(--white)}
.btn-pill{left:98px;top:296px;width:120px;height:40px;border-radius:20px;background:var(--blue);color:var(--white);font-size:14px;display:flex;align-items:center;justify-content:center}
.arrow{top:222px;width:30px;height:30px;border-radius:50%;background:rgba(255,255,255,.55);display:flex;align-items:center;justify-content:center}

.section-title{font-size:30px;font-weight:400;color:var(--blue-title);text-align:center}
.rule{left:573px;width:55px;height:3px;background:var(--blue)}

.about{top:644px;height:241px;background:var(--muted)}
.about p{left:160px;width:880px;top:118px;font-size:12.5px;line-height:22.4px;text-align:center;color:var(--ink)}

.products{top:885px;height:501px;background:var(--white)}
.sub{font-size:12.5px;color:var(--ink);text-align:center;line-height:23px}
.product{top:175px;width:223px;height:221px}
.product-label{top:194px;left:17px;width:188px;height:53px;background:var(--blue);color:var(--white);font-size:15px;font-weight:600;line-height:17px;text-align:center;display:flex;align-items:center;justify-content:center}

.services{top:1386px;height:527px;background:var(--muted)}
.service{top:199px;width:260px;text-align:center}
.service svg{display:block;margin:0 auto}
.service-label{margin-top:8px;font-size:15px;line-height:17px;color:var(--ink);text-transform:uppercase}

.faqs{top:1913px;height:339px;background:var(--white)}
.faq{width:489px;border-bottom:1px solid var(--line)}
.faq-q{display:flex;align-items:center;gap:11px;font-size:13.5px;color:var(--blue-title);height:26px}
.faq-a{font-size:12px;color:var(--ink);padding-left:35px;margin-top:4px}

.gap-band{top:2252px;height:60px;background:var(--muted)}

.contact{top:2312px;height:429px}
.contact-bg{background:linear-gradient(180deg,#2b93f4 0%,#1d84ea 45%,#1470cf 100%)}
.contact .section-title{color:var(--white)}
.contact .rule{background:var(--white)}
.contact .sub{color:var(--white)}
.field{background:var(--white);font-size:12px;color:#777;padding:10px 10px}
.captcha-code{right:10px;top:10px;font-size:12px;font-weight:600;color:#333}
.submit{left:907px;top:269px;width:132px;height:40px;border-radius:20px;background:var(--navy);color:var(--white);font-size:14px;display:flex;align-items:center;justify-content:center}

.footer{top:2741px;height:75px;background:var(--white);font-size:12.5px;color:var(--ink)}
.footer .domain{color:var(--blue)}
.to-top{left:582px;top:2722px;width:38px;height:38px;border-radius:50%;background:var(--navy);display:flex;align-items:center;justify-content:center;z-index:5}
</style>
</head>
<body>

<header class="section topbar">
  <div class="abs contact-item" style="left:98px">
    <svg width="13" height="13" viewBox="0 0 24 24"><path fill="#fff" d="M6.6 10.8a15.1 15.1 0 0 0 6.6 6.6l2.2-2.2c.3-.3.7-.4 1-.2 1.1.4 2.3.6 3.6.6.6 0 1 .4 1 1V20c0 .6-.4 1-1 1A17 17 0 0 1 3 4c0-.6.4-1 1-1h3.5c.6 0 1 .4 1 1 0 1.3.2 2.5.6 3.6.1.3 0 .7-.2 1l-2.3 2.2z"/></svg>
    <span>555-014-2290</span>
  </div>
  <div class="abs divider"></div>
  <div class="abs contact-item" style="left:216px">
    <svg width="13" height="10" viewBox="0 0 26 20"><rect x="1" y="1" width="24" height="18" fill="none" stroke="#fff" stroke-width="2"/><path d="M1 1l12 10L25 1" fill="none" stroke="#fff" stroke-width="2"/></svg>
    <span>hello@nordline.example</span>
  </div>
  <div class="abs social"><span></span><span></span><span></span><span></span></div>
</header>

<nav class="section header">
  <div class="abs brand">
    <div class="brand-mark"></div>
    <div>
      <div class="brand-name">Nordline</div>
      <div class="brand-tag">Your Trusted CBD Source</div>
    </div>
  </div>
  <div class="abs nav">
    <a href="#">HOME</a><span class="sep">|</span>
    <a href="#">ABOUT US</a><span class="sep">|</span>
    <a href="#">PRODUCTS</a><span class="sep">|</span>
    <a href="#">SERVICES</a><span class="sep">|</span>
    <a href="#">FAQS</a><span class="sep">|</span>
    <a href="#">CONTACT US</a>
  </div>
</nav>

<section class="section hero">
  <div class="fill hero-bg" role="img" aria-label="Photo of a hemp field at sunset under a soft sky"></div>
  <div class="fill hero-shade"></div>
  <h1 class="abs">WELCOME TO NORDLINE</h1>
  <p class="abs">At Nordline, our mission is to provide a seamless process for fulfilling all your CBD needs. We know that finding proper, reliable sourcing and manufacturing can be a headache, so we offer a full range of services, in addition to the highest quality CBD to make your experience effortless.</p>
  <div class="abs btn-pill">CONTACT US</div>
  <div class="abs arrow" style="left:8px"><svg width="12" height="12" viewBox="0 0 12 12"><path d="M8 1L3 6l5 5" fill="none" stroke="#333" stroke-width="2"/></svg></div>
  <div class="abs arrow" style="right:8px;opacity:.5"><svg width="12" height="12" viewBox="0 0 12 12"><path d="M4 1l5 5-5 5" fill="none" stroke="#333" stroke-width="2"/></svg></div>
</section>

<section class="section about">
  <h2 class="abs center section-title" style="top:46px">ABOUT US</h2>
  <div class="abs rule" style="top:94px"></div>
  <p class="abs">Based out of Denver, Colorado with over 5 years of experience in growing, setup and vetting only the highest quality sourcing allows discounted pricing for wholesale buyers. We have experience brokering and manufacturing from farm to finished product of both distillate and isolate. Due to the nature of the industry, labs often misrepresent their quality, production capabilities, and pricing. We believe in operating with full transparency.</p>
</section>

<section class="section products">
  <h2 class="abs center section-title" style="top:52px">PRODUCTS</h2>
  <div class="abs rule" style="top:100px"></div>
  <p class="abs center sub" style="top:119px">All locally sourced, organically grown hemp</p>

  <div class="abs product" style="left:98px">
    <div style="width:223px;height:221px;background:linear-gradient(160deg,#6a5746,#d9d9d6 45%,#f4f4f2 60%,#5e4b3c)" role="img" aria-label="Jar of white CBD isolate powder on wood"></div>
    <div class="abs product-label">CBD<br>ISOLATE 99.8+%</div>
  </div>
  <div class="abs product" style="left:357px">
    <div style="width:223px;height:221px;background:radial-gradient(circle at 50% 45%,#e2a33c 0%,#a8611a 35%,#131a4a 65%,#0b1038 100%)" role="img" aria-label="Swirl of golden distillate on a dark blue background"></div>
    <div class="abs product-label">T-FREE<br>DISTILATTE</div>
  </div>
  <div class="abs product" style="left:617px">
    <div style="width:223px;height:221px;background:linear-gradient(180deg,#e6e6e6 0%,#dcdcdc 40%,#6b3d1e 60%,#5a3316 90%,#e6e6e6 100%)" role="img" aria-label="Three amber CBD tincture dropper bottles"></div>
    <div class="abs product-label">CBD<br>TINCTURES</div>
  </div>
  <div class="abs product" style="left:878px">
    <div style="width:223px;height:221px;background:linear-gradient(120deg,#3fb2b2 0%,#7aa6b0 35%,#8a8f98 60%,#c9ccd1 100%)" role="img" aria-label="Lab technician operating extraction equipment"></div>
    <div class="abs product-label">WATER- SOLUBLE<br>ISOLATE &amp; DISTILLATE</div>
  </div>
</section>

<section class="section services">
  <h2 class="abs center section-title" style="top:52px">SERVICES</h2>
  <div class="abs rule" style="top:99px"></div>
  <p class="abs center sub" style="top:119px">We'd be happy to set up a schedule of delivery for your business so you are never out of stock.<br>White labeling services offered:</p>

  <div class="abs service" style="left:150px">
    <svg width="196" height="223" viewBox="0 0 196 223" role="img" aria-label="Cardboard boxes on a roller conveyor">
      <defs><linearGradient id="svcBox" x1="0" y1="0" x2="1" y2="1"><stop offset="0" stop-color="#d9c2a3"/><stop offset=".6" stop-color="#c99a5e"/><stop offset="1" stop-color="#b3b3b3"/></linearGradient></defs>
      <polygon points="98,3 193,57 193,166 98,220 3,166 3,57" fill="url(#svcBox)" stroke="#1186ef" stroke-width="4"/>
    </svg>
    <div class="service-label">Packaged<br>Isolate</div>
  </div>
  <div class="abs service" style="left:469px">
    <svg width="196" height="223" viewBox="0 0 196 223" role="img" aria-label="Pre-filled vape cartridge and its packaging">
      <defs><linearGradient id="svcVape" x1="0" y1="0" x2="1" y2="0"><stop offset="0" stop-color="#f4f4f4"/><stop offset=".35" stop-color="#2a2a2a"/><stop offset=".55" stop-color="#e8e8e8"/><stop offset=".68" stop-color="#e3c83a"/><stop offset="1" stop-color="#f4f4f4"/></linearGradient></defs>
      <polygon points="98,3 193,57 193,166 98,220 3,166 3,57" fill="url(#svcVape)" stroke="#1186ef" stroke-width="4"/>
    </svg>
    <div class="service-label">Pre-filled Vape<br>Cartridges</div>
  </div>
  <div class="abs service" style="left:788px">
    <svg width="196" height="223" viewBox="0 0 196 223" role="img" aria-label="Row of flavored tincture bottles">
      <defs><linearGradient id="svcTinc" x1="0" y1="0" x2="0" y2="1"><stop offset="0" stop-color="#ffffff"/><stop offset=".3" stop-color="#2a2a40"/><stop offset=".6" stop-color="#3b3f9a"/><stop offset=".85" stop-color="#ffffff"/></linearGradient></defs>
      <polygon points="98,3 193,57 193,166 98,220 3,166 3,57" fill="url(#svcTinc)" stroke="#1186ef" stroke-width="4"/>
    </svg>
    <div class="service-label">Bottled / Flavored<br>Tinctures</div>
  </div>
</section>

<section class="section faqs">
  <h2 class="abs center section-title" style="top:46px">FAQs</h2>
  <div class="abs rule" style="top:93px"></div>

  <div class="abs faq" style="left:98px;top:146px;height:37px">
    <div class="faq-q"><svg width="25" height="25" viewBox="0 0 26 26"><circle cx="13" cy="13" r="12" fill="none" stroke="#222" stroke-width="1.6"/><path d="M7 13h12M13 7v12" stroke="#222" stroke-width="1.6"/></svg>Does Nordline ship internationally?</div>
  </div>
  <div class="abs faq" style="left:612px;top:146px;height:37px">
    <div class="faq-q"><svg width="25" height="25" viewBox="0 0 26 26"><circle cx="13" cy="13" r="12" fill="none" stroke="#222" stroke-width="1.6"/><path d="M7 13h12M13 7v12" stroke="#222" stroke-width="1.6"/></svg>Does your isolate contain any THC?</div>
  </div>
  <div class="abs faq" style="left:98px;top:202px;height:37px">
    <div class="faq-q"><svg width="25" height="25" viewBox="0 0 26 26"><circle cx="13" cy="13" r="12" fill="none" stroke="#222" stroke-width="1.6"/><path d="M7 13h12M13 7v12" stroke="#222" stroke-width="1.6"/></svg>Can I do my own testing?</div>
  </div>
  <div class="abs faq" style="left:612px;top:202px;height:64px">
    <div class="faq-q"><svg width="25" height="25" viewBox="0 0 26 26"><circle cx="13" cy="13" r="12" fill="none" stroke="#222" stroke-width="1.6"/><path d="M7 13h12" stroke="#222" stroke-width="1.6"/></svg>Can I buy Pharma Grade CMP certified CBD?</div>
    <div class="faq-a">Yes, this is available upon request. Please reach out for further details</div>
  </div>
</section>

<div class="section gap-band"></div>

<section class="section contact">
  <div class="fill contact-bg" role="img" aria-label="Hemp field photo under a blue color overlay"></div>
  <h2 class="abs center section-title" style="top:39px">CONTACT US</h2>
  <div class="abs rule" style="top:85px"></div>
  <p class="abs center sub" style="top:104px">Contact us with any questions or for a quote</p>

  <div class="abs field" style="left:157px;top:156px;width:430px;height:149px">Message</div>
  <div class="abs field" style="left:612px;top:156px;width:429px;height:37px">Name</div>
  <div class="abs field" style="left:612px;top:213px;width:429px;height:37px">Email</div>
  <div class="abs field" style="left:612px;top:269px;width:285px;height:37px">Type the code shown<span class="abs captcha-code">HG845</span></div>
  <div class="abs submit">SUBMIT</div>
</section>

<footer class="section footer">
  <p class="abs center" style="top:38px">Copyright © 2019 <span class="domain">DOMAIN</span>. All Rights Reserved</p>
</footer>

<div class="abs to-top"><svg width="16" height="12" viewBox="0 0 16 12"><path d="M2 10l6-6 6 6" fill="none" stroke="#fff" stroke-width="3"/></svg></div>

</body>
</html>
```